Business card for event manager / organizer "waiter service"

Draft of a new valuable business card for my company.
Events, personnel service providers, festivals

```html
<!DOCTYPE html>
<html lang="de">
<head>
<meta charset="utf-8">
<title>Tafelwerk Service – Visitenkarte</title>
<link href="https://fonts.googleapis.com/css2?family=Montserrat:wght@400;500;600;800&display=swap" rel="stylesheet">
<style>
  :root {
    --backdrop: #c9c9c9;
    --card: #ffffff;
    --gold: #b8904a;
    --ink: #141414;
    --orange: #e8721c;
    --muted: #6b6b6b;
    --photo-top: #8a8f9a;
    --photo-bottom: #1e1e22;
  }
  * { margin: 0; padding: 0; box-sizing: border-box; }
  html, body { width: 1200px; height: 1200px; overflow: hidden; }
  body {
    background: var(--backdrop);
    font-family: "Montserrat", sans-serif;
    display: flex;
    flex-direction: column;
    align-items: center;
    justify-content: center;
    gap: 60px;
  }
  .card {
    position: relative;
    width: 860px;
    height: 500px;
    background: var(--card);
    box-shadow: 0 10px 30px rgba(0,0,0,0.18);
    overflow: hidden;
  }

  /* Front side */
  .holder { position: absolute; left: 64px; top: 62px; color: var(--gold); }
  .holder-name { font-size: 34px; font-weight: 600; letter-spacing: 0.5px; }
  .holder-role {
    display: inline-block;
    margin-top: 4px;
    font-size: 22px;
    font-weight: 400;
    padding-bottom: 6px;
    border-bottom: 2px solid var(--gold);
  }
  .contact-list {
    position: absolute;
    left: 64px;
    top: 228px;
    list-style: none;
    color: var(--gold);
    font-size: 21px;
    font-weight: 500;
  }
  .contact-list li { display: flex; align-items: center; gap: 14px; height: 34px; }
  .contact-list svg { width: 18px; height: 18px; flex: none; fill: var(--gold); }

  .brand { display: block; }
  .brand-row { display: flex; align-items: center; }
  .brand-mark { background: var(--orange); flex: none; }
  .brand-name { font-weight: 800; color: var(--ink); line-height: 1.05; letter-spacing: 0.5px; }
  .brand-tagline { color: var(--muted); font-weight: 400; white-space: nowrap; }

  .brand--front { position: absolute; left: 520px; top: 118px; }
  .brand--front .brand-row { gap: 12px; }
  .brand--front .brand-mark { width: 54px; height: 54px; }
  .brand--front .brand-name { font-size: 26px; }
  .brand--front .brand-tagline { font-size: 12px; margin-top: 10px; margin-left: 66px; }

  .portrait {
    position: absolute;
    left: 560px;
    top: 250px;
    width: 200px;
    height: 250px;
    background: linear-gradient(180deg, var(--photo-top), var(--photo-bottom));
  }

  /* Back side */
  .card--back { display: flex; align-items: center; justify-content: center; }
  .brand--back .brand-row { gap: 22px; }
  .brand--back .brand-mark { width: 110px; height: 110px; }
  .brand--back .brand-name { font-size: 50px; }
  .brand--back .brand-tagline { font-size: 18px; margin-top: 14px; margin-left: 132px; }
</style>
</head>
<body>

<section class="card card--front">
  <div class="holder">
    <div class="holder-name">Jonas Werthmann</div>
    <div class="holder-role">Inhaber</div>
  </div>

  <ul class="contact-list">
    <li>
      <svg viewBox="0 0 24 24"><path d="M6.6 10.8a15.1 15.1 0 0 0 6.6 6.6l2.2-2.2a1 1 0 0 1 1-.25 11.4 11.4 0 0 0 3.6.57 1 1 0 0 1 1 1V20a1 1 0 0 1-1 1A17 17 0 0 1 3 4a1 1 0 0 1 1-1h3.5a1 1 0 0 1 1 1c0 1.25.2 2.45.57 3.57a1 1 0 0 1-.25 1z"/></svg>
      02361 555 12 40
    </li>
    <li>
      <svg viewBox="0 0 24 24"><path d="M6.6 10.8a15.1 15.1 0 0 0 6.6 6.6l2.2-2.2a1 1 0 0 1 1-.25 11.4 11.4 0 0 0 3.6.57 1 1 0 0 1 1 1V20a1 1 0 0 1-1 1A17 17 0 0 1 3 4a1 1 0 0 1 1-1h3.5a1 1 0 0 1 1 1c0 1.25.2 2.45.57 3.57a1 1 0 0 1-.25 1z"/></svg>
      0170 555 83 27
    </li>
    <li>
      <svg viewBox="0 0 24 24"><path d="M2 5h20v2l-10 7L2 7z M2 9l10 7 10-7v10H2z"/></svg>
      info@tafelwerk-service.de
    </li>
    <li>
      <svg viewBox="0 0 24 24"><circle cx="12" cy="12" r="9" fill="none" stroke="#b8904a" stroke-width="2"/><path d="M3 12h18M12 3c3 3 3 15 0 18M12 3c-3 3-3 15 0 18" fill="none" stroke="#b8904a" stroke-width="2"/></svg>
      www.tafelwerk-service.de
    </li>
    <li>
      <svg viewBox="0 0 24 24"><path d="M12 2a7 7 0 0 0-7 7c0 5 7 13 7 13s7-8 7-13a7 7 0 0 0-7-7zm0 9.5A2.5 2.5 0 1 1 12 6.5a2.5 2.5 0 0 1 0 5z"/></svg>
      Lindenweg 14, 45657 Beispielstadt
    </li>
    <li>
      <svg viewBox="0 0 24 24"><circle cx="12" cy="12" r="9"/></svg>
      tafelwerkservice
    </li>
  </ul>

  <div class="brand brand--front">
    <div class="brand-row">
      <span class="brand-mark"></span>
      <span class="brand-name">TAFELWERK<br>SERVICE</span>
    </div>
    <div class="brand-tagline">…wir servieren Ihr Fest mit Stil!</div>
  </div>

  <div class="portrait" role="img" aria-label="Porträtfoto des Inhabers in Hemd und Weste mit verschränkten Armen"></div>
</section>

<section class="card card--back">
  <div class="brand brand--back">
    <div class="brand-row">
      <span class="brand-mark"></span>
      <span class="brand-name">TAFELWERK SERVICE</span>
    </div>
    <div class="brand-tagline">…wir servieren Ihr Fest mit Stil!</div>
  </div>
</section>

</body>
</html>
```